We need visit card and a letter paper for our website. thx

We have a beauty clinic in Switzerland.
https://wolkenbachtal.ch
We need a visit card.

Requirements
Must have
• see colors on website

```html
<!DOCTYPE html>
<html lang="de">
<head>
<meta charset="utf-8">
<title>Wolkenbachtal – Visitenkarte</title>
<link rel="stylesheet" href="https://fonts.googleapis.com/css2?family=Roboto:wght@300;400;500&display=swap">
<style>
  :root {
    --stage: #261418;
    --card-white: #ffffff;
    --card-pink: #f6c7d5;
    --pink-deep: #ecb3c4;
    --ink: #231f20;
    --skin: #d9a47e;
    --skin-light: #efd2bd;
  }
  * { box-sizing: border-box; margin: 0; padding: 0; }
  html, body { width: 1200px; height: 1200px; overflow: hidden; }
  body {
    background: var(--stage);
    font-family: "Roboto", sans-serif;
    color: var(--ink);
    position: relative;
  }
  .card { position: absolute; overflow: hidden; }

  /* Front */
  .card--front {
    left: 279px; top: 187px; width: 640px; height: 365px;
    background: var(--card-white);
  }
  .front__name {
    position: absolute; left: 0; right: 0; top: 100px;
    text-align: center;
    font-weight: 300; font-size: 56px; letter-spacing: 1px;
    color: var(--ink);
  }
  .front__photo {
    position: absolute; left: 30px; top: 205px; width: 580px; height: 160px;
    background: linear-gradient(180deg, rgba(255,255,255,0) 0%, var(--skin-light) 45%, var(--skin) 100%);
    border-radius: 80px 80px 0 0;
  }

  /* Back */
  .card--back {
    left: 290px; top: 648px; width: 617px; height: 356px;
    background: var(--card-pink);
  }
  .back__photo {
    position: absolute; inset: 0;
    background: radial-gradient(ellipse at 40% 55%, var(--pink-deep) 0%, var(--card-pink) 65%);
  }
  .back__brand {
    position: absolute; left: 20px; width: 220px; top: 86px;
    text-align: center; font-weight: 300; font-size: 24px;
  }
  .back__person { position: absolute; left: 309px; top: 72px; }
  .person__name { font-weight: 500; font-size: 29px; letter-spacing: 2px; line-height: 1; }
  .person__title { font-size: 14px; letter-spacing: 1.5px; margin-top: 6px; }
  .contact {
    position: absolute; top: 238px; font-size: 14.5px; line-height: 18px;
  }
  .contact--direct { right: calc(617px - 298px); text-align: right; }
  .contact--address { left: 314px; }
  .contact__divider {
    position: absolute; left: 305px; top: 236px; width: 1.5px; height: 54px; background: var(--ink);
  }
  .web-band {
    position: absolute; left: 36px; width: 545px; top: 296px; height: 27px;
    border-top: 1.5px solid var(--ink); border-bottom: 1.5px solid var(--ink);
    text-align: center; font-size: 14.5px; line-height: 24px;
  }
</style>
</head>
<body>
  <section class="card card--front">
    <div class="front__name">Wolkenbachtal</div>
    <div class="front__photo" role="img" aria-label="Photo of a woman in black swimwear reclining across the card"></div>
  </section>

  <section class="card card--back">
    <div class="back__photo" role="img" aria-label="Faint pink-toned photo of a woman lying on soft sheets"></div>
    <div class="back__brand">Wolkenbachtal</div>
    <div class="back__person">
      <div class="person__name">Dr. Lena Arnold</div>
      <div class="person__title">DESA</div>
    </div>
    <div class="contact contact--direct">
      <div>P. +41 (0) 800 22 40 60</div>
      <div>E: hallo@wolkenbachtal.ch</div>
    </div>
    <div class="contact__divider"></div>
    <div class="contact contact--address">
      <div>Talstrasse 8, 7500 Mittelbach</div>
      <div>Switzerland</div>
    </div>
    <div class="web-band">www.wolkenbachtal.ch</div>
  </section>
</body>
</html>
```